MOSLEN Environmental needs an upgrade to its current business cards design

We need an upgrade to our current business cards design, where the MOSLEN acronym is included, as possible and not being overloaded.
MOSLEN Environmental is an Environmental Consultancy Firm based in Sydney.
We would like to see creative designs different from the standard type of business cards (for example, rounded edges, different to standard size of common business cards.

Target Market(s)

industrial companies (oil & gas, petrochemical, mining, insolvency, finance and manufacturing), developers, architect firms, law firms.

Industry/Entity Type

Business

Contact Information for Business Card

logos (brand and acronym), if they don't appear overloaded.
name
role
name of company (MOSLEN Environmental),
address (Level 3, Suite 3C, 47-49 Dorrigan Lane, Wexmoor, NSW, 2188) landline (02 7314 2986)
mobile (staff member)
email (staff member) and
website (www.moslengreen.example).
Include: Contaminated Land, Site Remediation, Groundwater Assessment, Health and Ecological Risk Assessments, Acid Sulfate Soils, Waste Classification.

Font styles to use
Serif
Sans Serif

Requirements
Must have
• A creative design different to the standard type of business cards.
Nice to have
• Rounded edges
• Different size of business cards rather than the standard size.
Should not have
• Preferable not to use white colour background, unless it is required from a creative design proposed.
• Not an overloaded design.
• Avoid black colours

```html
<!DOCTYPE html>
<html lang="en">
<head>
<meta charset="utf-8">
<title>MOSLEN Environmental – Business Card</title>
<link rel="stylesheet" href="https://fonts.googleapis.com/css2?family=Roboto:wght@400;500;700&display=swap">
<style>
  :root {
    --backdrop: #e4e4e4;
    --card: #f6f6f6;
    --green: #93c81c;
    --green-deep: #84bb17;
    --grey: #6a6a6a;
    --grey-dark: #5b5b5b;
    --text: #555555;
    --white: #ffffff;
  }
  * { box-sizing: border-box; margin: 0; padding: 0; }
  html, body {
    width: 1200px; height: 576px; overflow: hidden;
    background: var(--backdrop);
    font-family: "Roboto", Arial, sans-serif;
    color: var(--text);
  }
  .canvas { position: relative; width: 1200px; height: 576px; }

  .card {
    position: absolute; top: 138px; width: 484px; height: 293px;
    background: var(--card); border-radius: 8px; overflow: hidden;
  }

  /* Back side: acronym + services */
  .card-back { left: 82px; }
  .card-back .services-panel {
    position: absolute; left: 224px; top: 0; right: 0; bottom: 0;
    background: linear-gradient(180deg, var(--green) 0%, var(--green-deep) 100%);
  }
  .card-back .pointer { position: absolute; left: 224px; top: 147px; }
  .acronym { position: absolute; left: 44px; top: 60px; list-style: none; }
  .acronym li { display: flex; align-items: center; height: 29px; }
  .acronym .initial {
    width: 32px; font-size: 28px; font-weight: 700; color: var(--grey); line-height: 1;
  }
  .acronym .word { font-size: 12.5px; font-weight: 700; color: var(--grey-dark); letter-spacing: 0.1px; }
  .services {
    position: absolute; left: 266px; top: 71px; list-style: none;
    color: var(--white); font-size: 14.4px; line-height: 22px;
  }
  .services li::before { content: "»"; font-size: 12px; margin-right: 8px; }

  /* Front side: contact */
  .card-front { left: 602px; }
  .brand-name {
    position: absolute; left: 25px; top: 38px;
    font-size: 27px; font-weight: 700; color: var(--green-deep); letter-spacing: 0.3px;
  }
  .person { position: absolute; right: 25px; top: 124px; text-align: right; }
  .person-name { font-size: 19.5px; font-weight: 700; color: var(--grey-dark); }
  .person-role { font-size: 12px; margin-top: 4px; }
  .divider { position: absolute; left: 25px; top: 166px; width: 326px; height: 1px; background: var(--green); }

  .office { position: absolute; left: 25px; top: 188px; font-size: 13px; line-height: 17.6px; list-style: none; }
  .office li { display: flex; align-items: flex-start; }
  .office .icon { width: 25px; padding-top: 3px; }
  .office .indent { padding-left: 25px; }

  .direct { position: absolute; right: 25px; top: 200px; font-size: 13px; line-height: 18px; list-style: none; text-align: right; }
  .direct li { display: flex; justify-content: flex-end; align-items: center; }
  .direct .icon { width: 17px; display: flex; justify-content: flex-end; }

  .footer-band { position: absolute; left: 0; bottom: 0; }
  .website {
    position: absolute; right: 25px; bottom: 11px;
    font-size: 12.5px; color: var(--white);
  }
</style>
</head>
<body>
<main class="canvas">

  <section class="card card-back" aria-label="Card back: acronym and services">
    <ul class="acronym">
      <li><span class="initial">M</span><span class="word">ANAGING</span></li>
      <li><span class="initial">O</span><span class="word">VERSIGHT (OF)</span></li>
      <li><span class="initial">S</span><span class="word">OIL,</span></li>
      <li><span class="initial">L</span><span class="word">AND (AND)</span></li>
      <li><span class="initial">E</span><span class="word">NVIRONMENTAL</span></li>
      <li><span class="initial">N</span><span class="word">EEDS</span></li>
    </ul>
    <div class="services-panel"></div>
    <svg class="pointer" width="15" height="26" viewBox="0 0 15 26" aria-hidden="true">
      <polygon points="0,0 15,13 0,26" fill="var(--card)"/>
    </svg>
    <ul class="services">
      <li>Contaminated Land</li>
      <li>Site Remediation</li>
      <li>Groundwater Assessment</li>
      <li>Health and Ecological</li>
      <li>Risk Assessments</li>
      <li>Acid Sulfate Soils</li>
      <li>Waste Classification</li>
    </ul>
  </section>

  <section class="card card-front" aria-label="Card front: contact details">
    <div class="brand-name">MOSLEN Environmental</div>

    <div class="person">
      <div class="person-name">Dorian Keller</div>
      <div class="person-role">Project Engineer</div>
    </div>
    <div class="divider"></div>

    <ul class="office">
      <li>
        <span class="icon">
          <svg width="13" height="11" viewBox="0 0 13 11" aria-hidden="true">
            <path d="M1 3.5 Q6.5 -0.5 12 3.5 L10.5 5 L8.5 3.8 L8.5 2.8 Q6.5 2 4.5 2.8 L4.5 3.8 L2.5 5 Z" fill="var(--green)"/>
            <rect x="3" y="5.5" width="7" height="5" rx="1" fill="var(--green)"/>
          </svg>
        </span>02 7314 2986
      </li>
      <li>
        <span class="icon">
          <svg width="11" height="14" viewBox="0 0 11 14" aria-hidden="true">
            <path d="M5.5 0 A5.5 5.5 0 0 1 11 5.5 C11 9 5.5 14 5.5 14 C5.5 14 0 9 0 5.5 A5.5 5.5 0 0 1 5.5 0 Z" fill="var(--green)"/>
            <circle cx="5.5" cy="5.3" r="2" fill="var(--card)"/>
          </svg>
        </span>Level 3, Suite 3C,
      </li>
      <li class="indent">47-49 Dorrigan Lane,</li>
      <li class="indent">Wexmoor, NSW, 2188</li>
    </ul>

    <ul class="direct">
      <li>0412 587 306
        <span class="icon">
          <svg width="9" height="13" viewBox="0 0 9 13" aria-hidden="true">
            <rect x="0" y="0" width="9" height="13" rx="1.5" fill="var(--green)"/>
            <rect x="1.5" y="2" width="6" height="7.5" fill="var(--card)"/>
          </svg>
        </span>
      </li>
      <li>dorian@moslengreen.example
        <span class="icon">
          <svg width="12" height="9" viewBox="0 0 12 9" aria-hidden="true">
            <rect width="12" height="9" fill="var(--green)"/>
            <polyline points="0,0 6,5 12,0" fill="none" stroke="var(--card)" stroke-width="1.2"/>
          </svg>
        </span>
      </li>
    </ul>

    <svg class="footer-band" width="484" height="40" viewBox="0 0 484 40" aria-hidden="true">
      <rect x="0" y="21" width="270" height="19" fill="var(--grey)"/>
      <polygon points="258,40 282,5 484,5 484,40" fill="var(--green)"/>
    </svg>
    <div class="website">www.moslengreen.example</div>
  </section>

</main>
</body>
</html>
```